Animated GIF banner for mobile app

We need a GIF Banner designed that alternates between two different ads.

Details are;
Pixel Size (W X H) 300 X 250
Minimum DPI 72dpi
File Size 40kb
File Size (Rich Media) 150kb

Ad 1 Text:
Lost super? More than one super fund? Contact us

Ad 2 Text:
Time to review your home loan? Contact us

Target Market(s)

30-55 year olds

Industry/Entity Type

Financial Service

Font styles to use
Sans Serif

Colors
0555a3
3176b5
85abd2

```html
<!DOCTYPE html>
<html lang="en">
<head>
<meta charset="utf-8">
<title>Daniel Hartley Financial Solutions – Banner Frames</title>
<link href="https://fonts.googleapis.com/css2?family=Arimo:wght@400;700&display=swap" rel="stylesheet">
<style>
  :root {
    --brand-dark: #0555a3;
    --brand-mid: #3176b5;
    --brand-light: #85abd2;
    --panel-top: #eef0f2;
    --panel-bottom: #c9cdd1;
    --copy-grey: #464646;
    --label-grey: #8a8a8a;
    --button-top: #ffd04a;
    --button-bottom: #f09a00;
    --arrow-orange: #f26a10;
    --white: #ffffff;
    --page-bg: #ffffff;
  }
  * { box-sizing: border-box; margin: 0; padding: 0; }
  html, body {
    width: 1200px; height: 1200px; overflow: hidden;
    background: var(--page-bg);
    font-family: "Arimo", Arial, sans-serif;
  }
  .sheet { position: relative; width: 1200px; height: 1200px; }

  .frame-label {
    position: absolute; left: 193px;
    font-size: 24px; color: var(--label-grey);
    letter-spacing: 0.5px; line-height: 1;
  }
  .frame-label--a { top: 369px; }
  .frame-label--b { top: 718px; }

  .banner-slot { position: absolute; left: 391px; width: 424px; height: 353px; }
  .banner-slot--a { top: 191px; }
  .banner-slot--b { top: 565px; }

  .banner {
    position: relative; width: 300px; height: 250px;
    transform: scale(1.4118); transform-origin: 0 0;
    border: 1px solid #2a3f60; overflow: hidden;
    background: var(--brand-light);
  }
  .banner__header {
    position: absolute; left: 0; top: 0; width: 100%; height: 50px;
    background: var(--brand-dark);
    display: flex; align-items: center; justify-content: center; gap: 8px;
  }
  .brand-mark { width: 22px; height: 22px; border-radius: 50%; background: var(--white); }
  .brand-name { color: var(--white); font-weight: 400; line-height: 1; }
  .brand-name__main { display: block; font-size: 20px; letter-spacing: -0.3px; }
  .brand-name__sub { display: block; font-size: 11px; margin-top: 2px; text-align: center; }

  .banner__tagline {
    position: absolute; left: 0; top: 50px; width: 100%; height: 40px;
    background: var(--brand-mid);
    color: var(--white); font-weight: 700; font-size: 13.5px;
    display: flex; align-items: center; justify-content: center;
    text-shadow: 0 1px 1px rgba(0,0,0,0.45);
  }

  .banner__message {
    position: absolute; left: 0; top: 90px; width: 150px; height: 113px;
    background: linear-gradient(to bottom, var(--panel-top), var(--panel-bottom));
    color: var(--copy-grey); font-weight: 700; text-align: center;
    text-shadow: 0 1px 0 rgba(255,255,255,0.8);
  }
  .message__question {
    position: absolute; left: 0; width: 100%;
    font-size: 16px; line-height: 16px;
  }
  .message__question--a { top: 16px; }
  .message__question--b { top: 10px; }
  .message__cta { position: absolute; left: 0; width: 100%; top: 79px; font-size: 16.5px; }

  .banner__photo {
    position: absolute; left: 148px; top: 90px; width: 152px; height: 113px;
    background:
      linear-gradient(to right, rgba(0,0,0,0.35) 0, rgba(0,0,0,0) 6px),
      linear-gradient(to bottom, #e3d6a8 0%, #c9ab6c 45%, #7f9a4a 70%, #5f8a35 100%);
  }

  .banner__footer {
    position: absolute; left: 0; top: 203px; width: 100%; height: 47px;
    background: var(--brand-light);
  }
  .cta-button {
    position: absolute; left: 41px; top: 4px; width: 212px; height: 34px;
    border-radius: 6px;
    background: linear-gradient(to bottom, var(--button-top), var(--button-bottom));
    box-shadow: 0 3px 4px rgba(0,0,0,0.35);
    color: var(--white); font-weight: 700; font-size: 12.5px;
    display: flex; align-items: center; padding-left: 10px; gap: 9px;
    text-shadow: 0 1px 1px rgba(120,60,0,0.6);
    letter-spacing: -0.2px;
  }
  .cta-button__icon { width: 22px; height: 22px; flex: none; }
</style>
</head>
<body>
<div class="sheet">

  <p class="frame-label frame-label--a">FRAME A</p>
  <div class="banner-slot banner-slot--a">
    <div class="banner">
      <div class="banner__header">
        <span class="brand-mark"></span>
        <span class="brand-name">
          <span class="brand-name__main">Daniel Hartley</span>
          <span class="brand-name__sub">Financial Solutions</span>
        </span>
      </div>
      <div class="banner__tagline">A NEW WAY TO FINANCIAL SOLUTIONS</div>
      <div class="banner__message">
        <p class="message__question message__question--a">Super Lost?<br>More Than One<br>Super fund?</p>
        <p class="message__cta">Contact Us</p>
      </div>
      <div class="banner__photo" role="img" aria-label="Photo of a couple embracing in front of their new home"></div>
      <div class="banner__footer">
        <div class="cta-button">
          <span>GET MORE INFORMATION</span>
          <svg class="cta-button__icon" viewBox="0 0 22 22" aria-hidden="true">
            <circle cx="11" cy="11" r="10.5" fill="#ffffff"/>
            <path d="M5.5 9.3h6V6l5.5 5-5.5 5v-3.3h-6z" fill="#f26a10"/>
          </svg>
        </div>
      </div>
    </div>
  </div>

  <p class="frame-label frame-label--b">FRAME B</p>
  <div class="banner-slot banner-slot--b">
    <div class="banner">
      <div class="banner__header">
        <span class="brand-mark"></span>
        <span class="brand-name">
          <span class="brand-name__main">Daniel Hartley</span>
          <span class="brand-name__sub">Financial Solutions</span>
        </span>
      </div>
      <div class="banner__tagline">A NEW WAY TO FINANCIAL SOLUTIONS</div>
      <div class="banner__message">
        <p class="message__question message__question--b">Time To<br>Review<br>Your home<br>Loan?</p>
        <p class="message__cta">Contact Us</p>
      </div>
      <div class="banner__photo" role="img" aria-label="Photo of a couple embracing in front of their new home"></div>
      <div class="banner__footer">
        <div class="cta-button">
          <span>GET MORE INFORMATION</span>
          <svg class="cta-button__icon" viewBox="0 0 22 22" aria-hidden="true">
            <circle cx="11" cy="11" r="10.5" fill="#ffffff"/>
            <path d="M5.5 9.3h6V6l5.5 5-5.5 5v-3.3h-6z" fill="#f26a10"/>
          </svg>
        </div>
      </div>
    </div>
  </div>

</div>
</body>
</html>
```